Marrowgate Auctions Business Cards Design Needed

I need a business card design that is modern looking - double sided (maybe just my logo on the back, but open to suggestions) - the overall design is up to you. I want it to be easy to read - not over the top flashy. I already have a company logo which I uploaded so that needs to be used. The colors of my logo are the colors I want on the card... so blue and gray (do need to match the logo colors).

Requirements
Must have
• Would like the card to be sleek, modern and easy to ready

```html
<!DOCTYPE html>
<html lang="en">
<head>
<meta charset="utf-8">
<title>Marrowgate Auctions – Business Cards</title>
<link href="https://fonts.googleapis.com/css2?family=Roboto:wght@400;500;700&family=Allura&display=swap" rel="stylesheet">
<style>
  :root {
    --brand-blue: #2a78c2;
    --brand-blue-light: #3f86cc;
    --brand-gray: #4b4c50;
    --ink: #333338;
    --paper: #ffffff;
    --paper-shade: #eceef2;
    --stage: #2b2b2d;
  }
  * { box-sizing: border-box; margin: 0; padding: 0; }
  html, body { width: 1200px; height: 900px; overflow: hidden; }
  body {
    background: var(--stage);
    font-family: "Roboto", Arial, sans-serif;
    display: flex;
    flex-direction: column;
    align-items: center;
    justify-content: center;
    gap: 42px;
  }
  .card {
    position: relative;
    width: 680px;
    height: 389px;
    border-radius: 18px;
    overflow: hidden;
  }

  /* ---------- Back ---------- */
  .card-back {
    background: linear-gradient(200deg, var(--brand-blue) 0%, var(--brand-blue-light) 35%, #3d6a97 65%, var(--brand-gray) 100%);
    color: var(--paper);
    display: flex;
    flex-direction: column;
    align-items: center;
    justify-content: center;
    text-align: center;
  }
  .card-back .wordmark { color: var(--paper); font-size: 42px; }
  .card-back .tagline { color: var(--paper); margin-top: 6px; font-size: 30px; }
  .card-back .web { margin-top: 30px; font-size: 16px; letter-spacing: 0.5px; }

  /* ---------- Shared wordmark ---------- */
  .wordmark {
    font-family: "Roboto", Arial, sans-serif;
    font-weight: 700;
    letter-spacing: 1px;
    text-transform: uppercase;
    line-height: 1;
  }
  .tagline {
    font-family: "Allura", cursive;
    line-height: 1.1;
  }

  /* ---------- Front ---------- */
  .card-front {
    background: linear-gradient(135deg, var(--paper) 0%, var(--paper) 55%, var(--paper-shade) 100%);
  }
  .front-brand { position: absolute; left: 44px; top: 46px; }
  .front-brand .wordmark { color: var(--brand-blue); font-size: 36px; }
  .front-brand .tagline { color: var(--brand-blue); margin-top: 8px; font-size: 28px; }

  .divider {
    position: absolute;
    left: 44px;
    right: 60px;
    top: 172px;
    height: 1px;
    background: var(--brand-gray);
  }
  .person { position: absolute; left: 44px; top: 188px; }
  .person .name {
    color: var(--brand-blue);
    font-weight: 700;
    font-size: 22px;
    letter-spacing: 0.5px;
    text-transform: uppercase;
  }
  .person .role { color: var(--ink); font-size: 15px; margin-top: 3px; }

  .contacts {
    position: absolute;
    right: 60px;
    top: 222px;
    list-style: none;
    text-align: right;
    color: var(--ink);
    font-size: 18px;
  }
  .contacts li { display: flex; align-items: center; justify-content: flex-end; gap: 10px; margin-bottom: 8px; }
  .contacts svg { width: 18px; height: 18px; fill: var(--brand-blue); }

  .bottom-band { position: absolute; left: 0; bottom: 0; width: 680px; height: 70px; }
  .bottom-band .band-blue { fill: var(--brand-blue); }
  .bottom-band .band-gray { fill: var(--brand-gray); }
  .front-web {
    position: absolute;
    right: 60px;
    bottom: 12px;
    color: var(--paper);
    font-size: 19px;
    letter-spacing: 0.5px;
  }
</style>
</head>
<body>

  <section class="card card-back">
    <div class="wordmark">Marrowgate Auctions</div>
    <div class="tagline">Elevating Benefit Auctions Coast to Coast</div>
    <div class="web">www.bidrevive.com</div>
  </section>

  <section class="card card-front">
    <div class="front-brand">
      <div class="wordmark">Marrowgate Auctions</div>
      <div class="tagline">Elevating Benefit Auctions Coast to Coast</div>
    </div>

    <div class="divider"></div>

    <div class="person">
      <div class="name">Nora Hale</div>
      <div class="role">Owner/President - Auctioneer</div>
    </div>

    <ul class="contacts">
      <li>702-555-0148
        <svg viewBox="0 0 24 24" aria-hidden="true"><path d="M6.6 10.8a15.1 15.1 0 0 0 6.6 6.6l2.2-2.2a1 1 0 0 1 1-.25 11.4 11.4 0 0 0 3.6.57 1 1 0 0 1 1 1V20a1 1 0 0 1-1 1A17 17 0 0 1 3 4a1 1 0 0 1 1-1h3.5a1 1 0 0 1 1 1c0 1.250.2 2.45.57 3.57a1 1 0 0 1-.25 1z"/></svg>
      </li>
      <li>marrowgateauctions@mail.com
        <svg viewBox="0 0 24 24" aria-hidden="true"><path d="M2 5h20v14H2z M4 7v.3l8 5.2 8-5.2V7z" fill-rule="evenodd"/></svg>
      </li>
    </ul>

    <svg class="bottom-band" viewBox="0 0 680 70" preserveAspectRatio="none" aria-hidden="true">
      <path class="band-gray" d="M0 34 H285 L318 50 H0 Z"/>
      <path class="band-blue" d="M0 58 H300 C335 58 340 30 380 30 H680 V70 H0 Z"/>
    </svg>
    <div class="front-web">www.bidrevive.com</div>
  </section>

</body>
</html>
```